PressLeaf repository plugin banner

There is a banner at the top of this page: https://pressleaf.example/addons/vexa-suite-signin/

It needs updating due to changes in the PressLeaf plugin repository display (e.g. there is no longer a border supplied around the banner) and also changes to Vexa Tools branding (which is now called 'V Bundle').

Otherwise, the existing banner concept works quite well - it shows the main part of the plugin functionality ('Login with Vexa') and also shows that it involves Vexa Tools (now called V Bundle) heavily.

I have attached a 'Login with Vexa' screenshot. Please find 'V Bundle' or 'Vexa' logos on Vexa's website or perhaps produce your own interpretation of their colors etc.

The appearance of the finished design should be 'clean and professional'.

I would like original design files and also PNGs at the following sizes:

1880 x 609
1544 x 500
940 x 304
772 x 250

To understand the current branding of our products, please see https://pl-vsignin.example/ - a lot of this is only semi-professional and may need updating, but the banner should fit in with that to some extent. Also the 96x96 icon on the plugin page will stay (four color triangles with a padlock).

Please also note the plugin is mainly for desktop computer users (not mobile really).

Thank you!

Rob
Updates

Project Deadline Extended
Reason: There haven't been many entries so far, and I would like to give more designers a chance to submit designs over the weekend. I will be online from Tuesday to intensively help any promising designs to be finalized! Good luck. Rob

Target Market(s)

IT professionals

Industry/Entity Type

Information Technology

Colors

Designer to choose colors to be used in the design.

Requirements
Must have
• Some kind of V Bundle / Vexa logo or coloring
• The 'Login with Vexa' button from my screenshot
Should not have
• Unnecessary words - it is not actually an advert!

```html
<!DOCTYPE html>
<html lang="en">
<head>
<meta charset="utf-8">
<title>PressLeaf plugin banner – Vexa sign-in</title>
<link rel="stylesheet" href="https://fonts.googleapis.com/css2?family=Allura&family=Open+Sans:wght@400;600&display=swap">
<style>
  :root {
    --navy: #001540;
    --ink: #3a3a3a;
    --ink-soft: #8a8a8a;
    --press-blue: #2a8bb8;
    --vexa-blue: #4d8ff0;
    --field-line: #d6d6d6;
  }
  * { margin: 0; padding: 0; box-sizing: border-box; }
  html, body { width: 1200px; height: 1200px; overflow: hidden; background: var(--navy); }
  .canvas { position: relative; width: 1200px; height: 1200px; background: var(--navy); }
  .banner {
    position: absolute; left: 0; top: 408px; width: 1200px; height: 390px; overflow: hidden;
    background: linear-gradient(100deg, #ececec 0%, #f9f9f9 35%, #ffffff 48%, #f1f1f1 75%, #dedede 100%);
  }
  .banner-art { position: absolute; inset: 0; width: 1200px; height: 390px; }
  .headline {
    position: absolute; left: 342px; top: 148px; width: 500px; text-align: center;
    font-family: "Allura", cursive; font-weight: 400; color: var(--ink); line-height: 1;
    white-space: nowrap;
  }
  .headline-main { font-size: 54px; display: block; }
  .headline-sub { font-size: 52px; display: block; margin-top: 4px; }
  .plugin-tag {
    position: absolute; left: 14px; bottom: 12px;
    display: flex; align-items: center; gap: 6px;
    font-family: "Open Sans", sans-serif; font-weight: 600; font-size: 15px; color: var(--ink);
  }
  .plugin-tag-square { width: 9px; height: 9px; background: var(--ink-soft); }
  .partner-tag {
    position: absolute; right: 16px; bottom: 24px;
    display: flex; align-items: center; gap: 6px;
    font-family: "Open Sans", sans-serif; font-weight: 600; font-size: 15px; color: var(--ink);
  }
  .partner-tag-dot { width: 10px; height: 10px; border-radius: 50%; background: var(--vexa-blue); }
  .ui text { font-family: "Open Sans", sans-serif; }
</style>
</head>
<body>
<div class="canvas">
  <section class="banner">
    <svg class="banner-art ui" viewBox="0 0 1200 390" xmlns="http://www.w3.org/2000/svg">
      <defs>
        <linearGradient id="leftFade" x1="0" x2="1" y1="0" y2="0">
          <stop offset="0" stop-color="#e6e6e6"/>
          <stop offset="0.8" stop-color="#f4f4f4"/>
          <stop offset="1" stop-color="#ffffff" stop-opacity="0"/>
        </linearGradient>
        <linearGradient id="rightFade" x1="0" x2="1" y1="0" y2="1">
          <stop offset="0" stop-color="#f6f6f6"/>
          <stop offset="1" stop-color="#d8d8d8"/>
        </linearGradient>
      </defs>

      <rect x="0" y="0" width="390" height="390" fill="url(#leftFade)" role="img" aria-label="Soft grey textured backdrop"/>
      <rect x="700" y="0" width="500" height="390" fill="url(#rightFade)" opacity="0.6" role="img" aria-label="Soft grey faceted backdrop"/>
      <rect x="990" y="0" width="210" height="208" fill="#f8f8f8" opacity="0.8"/>

      <g class="pressleaf-login">
        <circle cx="108" cy="33" r="5" fill="var(--press-blue)"/>
        <text x="117" y="37" font-size="11" fill="var(--press-blue)" font-weight="600">PressLeaf</text>
        <rect x="84" y="54" width="99" height="104" fill="#fff"/>
        <rect x="91" y="62" width="85" height="11" fill="var(--press-blue)"/>
        <text x="133.5" y="70" font-size="5" fill="#fff" text-anchor="middle" font-weight="600">Login with Vexa</text>
        <text x="133.5" y="84" font-size="4.5" fill="var(--ink)" text-anchor="middle">or</text>
        <text x="91" y="93" font-size="3.8" fill="var(--ink-soft)">Username or Email Address</text>
        <rect x="91" y="96" width="85" height="10" fill="#fbfbfb" stroke="var(--field-line)" stroke-width="0.6"/>
        <text x="91" y="115" font-size="3.8" fill="var(--ink-soft)">Password</text>
        <rect x="91" y="118" width="85" height="11" fill="#fbfbfb" stroke="var(--field-line)" stroke-width="0.6"/>
        <rect x="91" y="136" width="4" height="4" fill="#fff" stroke="var(--field-line)" stroke-width="0.6"/>
        <text x="98" y="139.5" font-size="3.5" fill="var(--ink-soft)">Remember Me</text>
        <rect x="156" y="134" width="20" height="10" fill="var(--press-blue)"/>
        <text x="166" y="140.5" font-size="4" fill="#fff" text-anchor="middle">Log In</text>
        <text x="91" y="170" font-size="3.8" fill="var(--ink-soft)">Lost your password?</text>
        <text x="91" y="181" font-size="3.8" fill="var(--ink-soft)">← Back to PressLeaf Site</text>
      </g>

      <g class="vexa-signin">
        <text x="851" y="15" font-size="12" fill="var(--vexa-blue)" text-anchor="middle">Vexa</text>
        <text x="851" y="30" font-size="5.5" fill="#555" text-anchor="middle">Sign in with your Vexa Account</text>
        <rect x="801" y="38" width="101" height="86" fill="#fafafa" stroke="#e4e4e4" stroke-width="0.6"/>
        <circle cx="851" cy="56" r="12" fill="#d8d8d8"/>
        <rect x="808" y="78" width="86" height="14" fill="#fff" stroke="var(--vexa-blue)" stroke-width="0.8"/>
        <text x="811" y="87.5" font-size="5" fill="#999">Enter your email</text>
        <rect x="808" y="95" width="86" height="11" fill="var(--vexa-blue)"/>
        <text x="851" y="102.5" font-size="4.5" fill="#fff" text-anchor="middle" font-weight="600">Next</text>
        <text x="894" y="115" font-size="4" fill="var(--vexa-blue)" text-anchor="end">Need help?</text>
        <text x="851" y="135" font-size="4.5" fill="var(--vexa-blue)" text-anchor="middle">Create account</text>
        <text x="851" y="151" font-size="4.2" fill="#777" text-anchor="middle">One Vexa Account for everything Vexa</text>
        <g fill="#c4c4c4">
          <rect x="816" y="155" width="5" height="5"/><rect x="827" y="155" width="5" height="5"/>
          <rect x="838" y="155" width="5" height="5"/><rect x="849" y="155" width="5" height="5"/>
          <rect x="860" y="155" width="5" height="5"/><rect x="871" y="155" width="5" height="5"/>
          <rect x="882" y="155" width="5" height="5"/>
        </g>
      </g>

      <g class="vexa-consent">
        <text x="1072" y="35" font-size="4.8" fill="#999" text-anchor="middle">· Northwind Intranet would like to:</text>
        <g font-size="3.8" fill="#666">
          <circle cx="1016" cy="53" r="3" fill="#9cb8e8"/><text x="1025" y="55">Know who you are on Vexa</text>
          <circle cx="1129" cy="53" r="2.5" fill="none" stroke="#bbb" stroke-width="0.5"/>
          <line x1="1008" y1="64" x2="1136" y2="64" stroke="#e6e6e6" stroke-width="0.6"/>
          <circle cx="1016" cy="74" r="3" fill="#9cb8e8"/><text x="1025" y="76">View your email address</text>
          <circle cx="1129" cy="74" r="2.5" fill="none" stroke="#bbb" stroke-width="0.5"/>
          <line x1="1008" y1="85" x2="1136" y2="85" stroke="#e6e6e6" stroke-width="0.6"/>
          <circle cx="1016" cy="95" r="3" fill="#9cb8e8"/><text x="1025" y="97">View your basic profile info</text>
          <circle cx="1129" cy="95" r="2.5" fill="none" stroke="#bbb" stroke-width="0.5"/>
          <line x1="1008" y1="106" x2="1136" y2="106" stroke="#e6e6e6" stroke-width="0.6"/>
        </g>
        <g font-size="2.8" fill="#888">
          <text x="1010" y="118">By clicking Accept, you allow this app and Vexa to use your details in</text>
          <text x="1010" y="122">line with their own terms of service and privacy rules. You can</text>
          <text x="1010" y="126">change this and other account settings at any time.</text>
        </g>
        <rect x="1088" y="136" width="20" height="9" fill="#f2f2f2" stroke="#ddd" stroke-width="0.5"/>
        <text x="1098" y="141.5" font-size="3" fill="#666" text-anchor="middle">Cancel</text>
        <rect x="1114" y="136" width="21" height="9" fill="var(--vexa-blue)"/>
        <text x="1124.5" y="141.5" font-size="3" fill="#fff" text-anchor="middle">Accept</text>
      </g>
    </svg>

    <h1 class="headline">
      <span class="headline-main">YOUR TEXT HERE</span>
      <span class="headline-sub">PLv</span>
    </h1>

    <div class="plugin-tag"><span class="plugin-tag-square"></span>PLv</div>
    <div class="partner-tag"><span class="partner-tag-dot"></span>Vexa</div>
  </section>
</div>
</body>
</html>
```